Bright Stride Journal,Tampa Edition. We are a very high end local free health and fitness magazine

We are a very high end local (Tampa, FL) free health and fitness magazine and need a "media kit" postcard to give to prospective advertisers (business owners and services) about why they should advertise in our magazine. We want to emphasize that fit people use ALL types of services and products, not just fitness and health services and products. Having their ad in the magazine will put them on the map and above their competition.
I uploaded a few covers, but of course you don't have to use all of them. I just wanted to give you options.

I need room somewhere for the contact info.

```html
<!DOCTYPE html>
<html lang="en">
<head>
<meta charset="utf-8">
<title>Bright Stride Journal – Advertiser Postcard</title>
<link href="https://fonts.googleapis.com/css2?family=Oswald:wght@400;500;600&family=Open+Sans:wght@300;400;700&display=swap" rel="stylesheet">
<style>
  :root {
    --purple: #9a63b3;
    --purple-deep: #7b3f98;
    --teal: #2db6a3;
    --teal-light: #b7e3dc;
    --white: #ffffff;
    --page: #e9e9ec;
  }
  * { margin: 0; padding: 0; box-sizing: border-box; }
  html, body { width: 1200px; height: 900px; overflow: hidden; background: var(--page); }
  .postcard {
    position: absolute; left: 60px; top: 80px;
    width: 1080px; height: 740px;
    background: var(--white); overflow: hidden;
    box-shadow: 0 10px 30px rgba(0,0,0,.18);
  }
  .postcard__shapes { position: absolute; inset: 0; }
  .hero-photo {
    position: absolute; left: 300px; top: 70px; width: 300px; height: 670px;
    background: linear-gradient(180deg, #f3dccb 0%, #b98fc8 45%, #4cc1ae 85%, #f7f7f7 100%);
    border-radius: 140px 140px 0 0;
    opacity: .85;
  }
  .photo-overlay { position: absolute; inset: 0; pointer-events: none; }
  .promo {
    position: absolute; left: 66px; top: 150px; width: 230px;
    font-family: 'Oswald', sans-serif;
  }
  .promo__title { color: var(--teal); font-weight: 500; font-size: 19px; letter-spacing: .3px; margin-bottom: 18px; }
  .promo__body { color: var(--purple-deep); font-weight: 500; font-size: 20px; line-height: 1.38; }
  .brand-box {
    position: absolute; left: 620px; top: 40px; width: 270px; height: 230px;
    background: var(--white);
    display: flex; flex-direction: column; justify-content: center; align-items: center;
  }
  .brand-box__name {
    font-family: 'Oswald', sans-serif; font-weight: 600; color: var(--teal);
    font-size: 66px; line-height: 1; text-align: center; letter-spacing: 1px;
  }
  .offer {
    position: absolute; left: 640px; top: 410px; width: 410px;
    color: var(--white); font-family: 'Open Sans', sans-serif;
  }
  .offer__headline { font-weight: 300; font-size: 25px; line-height: 1.12; text-transform: uppercase; }
  .offer__contact { font-weight: 700; font-size: 24px; margin-top: 14px; }
  .offer__text { font-size: 14px; line-height: 1.4; margin-top: 4px; }
  .contact-icons { display: flex; justify-content: space-between; margin-top: 36px; width: 380px; }
  .contact-item { width: 110px; text-align: center; }
  .contact-item__icon {
    width: 40px; height: 40px; border-radius: 50%; background: var(--purple);
    margin: 0 auto 10px; display: flex; align-items: center; justify-content: center;
  }
  .contact-item__label { font-family: 'Open Sans', sans-serif; font-size: 10px; line-height: 1.3; }
</style>
</head>
<body>
  <main class="postcard">
    <svg class="postcard__shapes" viewBox="0 0 1080 740" width="1080" height="740">
      <rect class="edge-strip" x="0" y="0" width="42" height="740" fill="var(--purple)"/>
      <polygon class="corner-accent" points="0,680 70,740 0,740" fill="var(--teal)"/>
      <rect class="divider-band" x="480" y="0" width="120" height="740" fill="var(--purple)"/>
      <polygon class="top-corner" points="870,0 1080,0 1080,110" fill="var(--purple)"/>
      <polygon class="contact-panel" points="600,390 1080,110 1080,740 600,740" fill="var(--teal)"/>
    </svg>

    <div class="hero-photo" role="img" aria-label="Photo of a smiling fitness model in a purple and teal sports top and shorts"></div>

    <svg class="photo-overlay" viewBox="0 0 1080 740" width="1080" height="740">
      <polygon points="330,740 600,390 600,740" fill="var(--teal-light)" opacity=".55"/>
    </svg>

    <section class="promo">
      <h2 class="promo__title">WHY ADVERTISE WITH US</h2>
      <p class="promo__body">Fit people don't only buy gym passes. They dine out, buy homes, book salons, lease cars, plan travel and hire lawyers, dentists and builders. Our free, high-end Tampa magazine lands in the hands of active, affluent readers who spend on every kind of product and service. Put your business in front of them.</p>
    </section>

    <div class="brand-box">
      <p class="brand-box__name">BRIGHT<br>STRIDE</p>
    </div>

    <section class="offer">
      <h1 class="offer__headline">Put your business<br>on the map &amp;<br>above the competition</h1>
      <p class="offer__contact">Your Contact Info Here</p>
      <p class="offer__text">Ask for our Tampa Edition media kit, ad sizes and rates. Restaurants, retail, real estate, auto and more.</p>
      <div class="contact-icons">
        <div class="contact-item">
          <div class="contact-item__icon">
            <svg width="18" height="18" viewBox="0 0 24 24"><circle cx="12" cy="8" r="4.5" fill="#fff"/><path d="M3 22c0-5 4-8 9-8s9 3 9 8z" fill="#fff"/></svg>
          </div>
          <p class="contact-item__label">Call our ad team</p>
        </div>
        <div class="contact-item">
          <div class="contact-item__icon">
            <svg width="18" height="18" viewBox="0 0 24 24"><circle cx="10" cy="10" r="6" fill="none" stroke="#fff" stroke-width="3"/><line x1="14.5" y1="14.5" x2="21" y2="21" stroke="#fff" stroke-width="3" stroke-linecap="round"/></svg>
          </div>
          <p class="contact-item__label">Find us in Tampa</p>
        </div>
        <div class="contact-item">
          <div class="contact-item__icon">
            <svg width="18" height="18" viewBox="0 0 24 24"><path d="M12 3 2 12h3v9h5v-6h4v6h5v-9h3z" fill="#fff"/></svg>
          </div>
          <p class="contact-item__label">Visit our website</p>
        </div>
      </div>
    </section>
  </main>
</body>
</html>
```